Korvix App Graphics Design

Our application promotes location based self expression via pictures and text. The primary focus of the application is on the content posted and not on the person that posted it.

We want a very clean and fresh design that evokes positive energy. Our site is unique so our design should be as well. People will reveal thoughts on our site, so the design should convey a "revealing" feel. Our site is a place where people are comfortable to freely express themselves. Colors we have in mind are blue and green hues with earth tones for background.

Our project is to design ten screens for our Korvix application at resolution of 1136-by-640 pixels:

Feed Screen
Camera Screen
Post Screen
Check In Screen
Approval Screen
Map Screen
Flag Screen
Feed Select Screen
Export Screen
Menu Screen

In the contest phase we will require only three screens to be submitted. The screens we require to be submitted are: Feed Screen; Map Screen and Camera Screen. The designer we select as the winner of the competition will then complete the project and deliver a total of the ten screens described above in the handover phase.

We have attached a document below with detailed specs of each screen, we ask for your innovation to bring these screens to life through your design.
Updates

We want to clarify one aspect regarding the VISOR: the visor needs to be transparent so that when the picture scrolls underneath it, you can still see the picture underneath the visor.

Hi Everyone,

We have noticed that some designers need clarification regarding the visor element in the feed screen.
I have attached two examples to our brief area called:
Visor Example 1 and Visor Example 2

Please note that these are not the style we are looking for but are a good example to the concept of a Transparent Visor above the feed stream. We are looking for you guys to come up with a Visor concept that is consistent with the style of the design you are submitting.

Thanks,

Bo

Target Market(s)

People 17-40 who want to share their thought about the world around them.

Industry/Entity Type

Flag

Font styles to use
Sans Serif
Other font styles liked:
• We like “Helvetica New” or “Avenir” but are flexible

Requirements
Must have
• Visor component should look innovative.

```html
<!DOCTYPE html>
<html lang="en">
<head>
<meta charset="utf-8">
<title>Korvix – Camera Screen</title>
<link rel="stylesheet" href="https://fonts.googleapis.com/css2?family=Inter:wght@400;500&display=swap">
<style>
  :root {
    --status-bg: #000000;
    --bar-navy: #03033a;
    --band-light: #d9d9d9;
    --strip-grey: #a9a9a9;
    --thumb-fill: #1c1c1c;
    --white: #ffffff;
    --shutter: #ff5a00;
    --battery: #3fc23f;
    --status-text: #d8d8d8;
  }
  * { box-sizing: border-box; margin: 0; padding: 0; }
  html, body {
    width: 676px; height: 1200px; overflow: hidden;
    background: var(--bar-navy);
    font-family: "Inter", "Helvetica Neue", Arial, sans-serif;
  }
  .screen { position: relative; width: 676px; height: 1200px; overflow: hidden; }

  .status-bar {
    position: absolute; top: 0; left: 0; width: 676px; height: 42px;
    background: var(--status-bg); color: var(--status-text);
    display: flex; align-items: center; justify-content: space-between;
    padding: 0 12px 0 10px; font-size: 26px; font-weight: 400;
  }
  .status-left, .status-right { display: flex; align-items: center; gap: 8px; }
  .signal { display: flex; gap: 3px; }
  .signal span { width: 13px; height: 13px; border-radius: 50%; background: var(--status-text); }
  .signal span.empty { background: none; border: 1.5px solid var(--status-text); }

  .top-toolbar {
    position: absolute; top: 42px; left: 0; width: 676px; height: 127px;
    background: var(--bar-navy);
  }
  .tool { position: absolute; top: 40px; width: 50px; height: 50px; }

  .band { position: absolute; left: 0; width: 676px; background: var(--band-light); }
  .band-top { top: 169px; height: 26px; }

  .viewfinder {
    position: absolute; top: 195px; left: 0; width: 676px; height: 611px;
    background:
      linear-gradient(180deg, #f2c56a 0%, #e3a24e 14%, #6a5a48 30%, #3b3a3a 55%, #5b6e78 75%, #3a3230 100%);
  }

  .filter-tray { position: absolute; top: 806px; left: 0; width: 676px; height: 210px; }
  .filter-tray svg { position: absolute; top: 0; left: 0; }
  .thumb {
    position: absolute; top: 65px; width: 119px; height: 119px;
    background: var(--thumb-fill); border: 4px solid var(--white); border-radius: 13px;
  }

  .bottom-toolbar {
    position: absolute; top: 1016px; left: 0; width: 676px; height: 184px;
    background: var(--bar-navy);
  }
  .control { position: absolute; top: 85px; width: 52px; height: 52px; }
  .shutter {
    position: absolute; left: 274px; top: 23px; width: 130px; height: 130px;
    border-radius: 50%; background: var(--white);
    display: flex; align-items: center; justify-content: center;
  }
  .shutter span {
    width: 110px; height: 110px; border-radius: 50%;
    background: var(--shutter); box-shadow: inset 0 -3px 6px rgba(0,0,0,.2);
  }
</style>
</head>
<body>
<div class="screen">

  <header class="status-bar">
    <div class="status-left">
      <div class="signal"><span></span><span></span><span></span><span></span><span class="empty"></span></div>
      <span class="carrier">NIMBUS</span>
      <svg width="28" height="20" viewBox="0 0 28 20" aria-hidden="true">
        <path d="M2 7a17 17 0 0 1 24 0M6 11a11 11 0 0 1 16 0M10 15a5 5 0 0 1 8 0" fill="none" stroke="#d8d8d8" stroke-width="3"/>
        <circle cx="14" cy="18" r="2" fill="#d8d8d8"/>
      </svg>
    </div>
    <div class="status-right">
      <svg width="16" height="24" viewBox="0 0 16 24" aria-hidden="true">
        <path d="M2 7l11 10-5 5V2l5 5L2 17" fill="none" stroke="#8a8a8a" stroke-width="2"/>
      </svg>
      <span class="battery-level">82%</span>
      <svg width="58" height="24" viewBox="0 0 58 24" aria-hidden="true">
        <rect x="1" y="2" width="48" height="20" rx="3" fill="none" stroke="#d8d8d8" stroke-width="2"/>
        <rect x="4" y="5" width="38" height="14" fill="#3fc23f"/>
        <rect x="50" y="8" width="3" height="8" fill="#d8d8d8"/>
        <path d="M57 4l-4 9h3l-2 8" fill="none" stroke="#d8d8d8" stroke-width="2"/>
      </svg>
    </div>
  </header>

  <nav class="top-toolbar">
    <svg class="tool flash-off" style="left:44px" viewBox="0 0 50 50" aria-label="Flash off">
      <path d="M18 2L6 26h11l-5 22 18-30H19l8-16z" fill="#fff"/>
      <circle cx="38" cy="38" r="8" fill="none" stroke="#fff" stroke-width="3"/>
      <line x1="33" y1="43" x2="43" y2="33" stroke="#fff" stroke-width="3"/>
    </svg>
    <svg class="tool switch-camera" style="left:220px;width:58px" viewBox="0 0 58 50" aria-label="Switch camera">
      <path d="M4 12h12l5-7h16l5 7h12v34H4z" fill="#fff"/>
      <path d="M19 27a10 10 0 0 1 18-5M39 28a10 10 0 0 1-18 5" fill="none" stroke="#03033a" stroke-width="3.5"/>
      <path d="M38 16v8h-8z M20 40v-8h8z" fill="#03033a"/>
    </svg>
    <svg class="tool focus" style="left:405px" viewBox="0 0 50 50" aria-label="Focus">
      <circle cx="25" cy="25" r="17" fill="none" stroke="#fff" stroke-width="4" stroke-dasharray="18 8.7" stroke-dashoffset="9"/>
      <path d="M25 1v12M25 37v12M1 25h12M37 25h12" stroke="#fff" stroke-width="4"/>
    </svg>
    <svg class="tool close" style="left:587px" viewBox="0 0 50 50" aria-label="Close">
      <path d="M6 6l38 38M44 6L6 44" stroke="#fff" stroke-width="6" stroke-linecap="round"/>
    </svg>
  </nav>

  <div class="band band-top"></div>

  <div class="viewfinder" role="img" aria-label="Live camera preview: aerial view of a city downtown at sunset with towers and lit streets"></div>

  <section class="filter-tray">
    <svg width="676" height="210" viewBox="0 0 676 210" aria-hidden="true">
      <rect width="676" height="210" fill="#a9a9a9"/>
      <path d="M0 0H676V36 L668 30 L657 40 L646 30 L635 40 L624 30 L613 40 L602 30 L591 40 L580 30 L569 40 L558 30 L547 40 L536 30 L525 40 L514 30 L503 40 L492 30 L481 40 L470 30 L459 40 L448 30 L437 40 L426 30 L415 40 L404 30 L393 40 L382 30 L371 40 L360 30 L349 40 L338 30 L327 40 L316 30 L305 40 L294 30 L283 40 L272 30 L261 40 L250 30 L239 40 L228 30 L217 40 L206 30 L195 40 L184 30 L173 40 L162 30 L151 40 L140 30 L129 40 L118 30 L107 40 L96 30 L85 40 L74 30 L63 40 L52 30 L41 40 L30 30 L19 40 L8 30 L0 36Z" fill="#d9d9d9"/>
    </svg>
    <div class="thumb" style="left:26px"></div>
    <div class="thumb" style="left:176px"></div>
    <div class="thumb" style="left:326px"></div>
    <div class="thumb" style="left:476px"></div>
    <div class="thumb" style="left:626px"></div>
  </section>

  <nav class="bottom-toolbar">
    <svg class="control rotate" style="left:46px" viewBox="0 0 52 52" aria-label="Rotate">
      <path d="M40 18A17 17 0 1 0 43 30" fill="none" stroke="#fff" stroke-width="5" stroke-linecap="round"/>
      <path d="M45 6v16H29z" fill="#fff"/>
    </svg>
    <svg class="control brightness" style="left:156px" viewBox="0 0 52 52" aria-label="Brightness">
      <circle cx="26" cy="26" r="12" fill="none" stroke="#fff" stroke-width="4"/>
      <path d="M26 14a12 12 0 0 1 0 24z" fill="#fff"/>
      <path d="M26 2v7M26 43v7M2 26h7M43 26h7M9 9l5 5M38 38l5 5M43 9l-5 5M14 38l-5 5" stroke="#fff" stroke-width="4" stroke-linecap="round"/>
    </svg>
    <div class="shutter" aria-label="Take photo"><span></span></div>
    <svg class="control crop" style="left:471px" viewBox="0 0 52 52" aria-label="Crop">
      <path d="M13 2v37h37M2 13h37v37" fill="none" stroke="#fff" stroke-width="5"/>
      <path d="M40 6L10 42" stroke="#fff" stroke-width="3"/>
    </svg>
    <svg class="control enhance" style="left:580px" viewBox="0 0 52 52" aria-label="Enhance">
      <path d="M24 24l24 24" stroke="#fff" stroke-width="6" stroke-linecap="round"/>
      <path d="M20 2v8M20 30v8M2 20h8M30 20h8M7 7l5 5M33 7l-5 5M7 33l5-5" stroke="#fff" stroke-width="4" stroke-linecap="round"/>
    </svg>
  </nav>

</div>
</body>
</html>
```